letterhead design using our existing logo

We are a small boutique property management business based in Sydney's Northern Beaches.
We are after a sleek, simple modern letterhead (A4) incorporating our logo and its colours.
Also matching envelope (DL)
I have attached the logo with black text and white text for design options.

Target Market(s)

29-69yo Male and Female

Industry/Entity Type

Property Management

Requirements
Must have
• - Keyhaven Estates logo
• - Address, number and website:
• Suite 7, 18-19 Harlow Parade, Brookvale NSW 2100
• Tel: Tom Carrick 0417 293 608 Lorena Adcock 0409 516 742 www.keyhavenestatesgroup.com.au
Nice to have
• sleek design that looks modern and professional
Should not have
• too many colours or too busy

```html
<!DOCTYPE html>
<html lang="en">
<head>
<meta charset="utf-8">
<title>Keyhaven Estates – Letterhead and DL Envelope</title>
<link href="https://fonts.googleapis.com/css2?family=Arimo:wght@400;700&display=swap" rel="stylesheet">
<style>
  :root {
    --teal: #177d8e;
    --teal-light: #2aa3b0;
    --ink: #1a1a1a;
    --paper: #ffffff;
    --paper-edge: #dcdcdc;
    --backdrop: #eceeef;
  }
  * { box-sizing: border-box; margin: 0; padding: 0; }
  html, body { width: 1200px; height: 1000px; overflow: hidden; }
  body {
    position: relative;
    background: var(--backdrop);
    font-family: "Arimo", Arial, sans-serif;
    color: var(--ink);
  }
  .sheet {
    position: absolute;
    background: var(--paper);
    border: 1px solid var(--paper-edge);
    overflow: hidden;
  }
  .letterhead { left: 30px; top: 78px; width: 597px; height: 844px; }
  .envelope-front { left: 540px; top: 190px; width: 623px; height: 310px; }
  .envelope-back { left: 540px; top: 520px; width: 623px; height: 310px; }

  .brand {
    position: absolute;
    display: flex;
    align-items: center;
    gap: 8px;
  }
  .brand-name {
    font-weight: 700;
    font-size: 23px;
    letter-spacing: -0.2px;
    text-transform: uppercase;
    color: var(--ink);
  }
  .brand-dot {
    width: 14px; height: 14px;
    border-radius: 50%;
    background: var(--teal);
  }
  .letterhead .brand { left: 26px; top: 58px; }
  .envelope-front .brand { left: 22px; top: 60px; }

  .contact-bar {
    position: absolute;
    left: 0; right: 0;
    height: 26px;
    font-size: 10.5px;
    line-height: 13px;
  }
  .letterhead .contact-bar { bottom: 20px; }
  .envelope-front .contact-bar { bottom: 18px; }

  .contact-block {
    position: absolute;
    top: 0;
    white-space: nowrap;
  }
  .contact-divider {
    position: absolute;
    top: 2px;
    width: 2px;
    height: 22px;
    background: var(--teal-light);
  }

  /* Letterhead footer columns */
  .letterhead .block-address { left: 26px; }
  .letterhead .divider-one { left: 194px; }
  .letterhead .block-phones { left: 230px; }
  .letterhead .divider-two { left: 394px; }
  .letterhead .block-web { left: 417px; }

  /* Envelope footer columns */
  .envelope-front .block-address { left: 26px; }
  .envelope-front .divider-one { left: 199px; }
  .envelope-front .block-phones { left: 242px; }
  .envelope-front .divider-two { left: 411px; }
  .envelope-front .block-web { left: 436px; }

  .edge-stripe {
    position: absolute;
    left: 0; right: 0; bottom: 0;
    height: 10px;
    background: linear-gradient(var(--teal-light) 0 50%, var(--teal) 50% 100%);
  }
  .envelope-front .edge-stripe { height: 8px; }

  .flap {
    position: absolute;
    left: 0; top: 0;
    width: 623px; height: 108px;
    background: var(--teal);
    border-radius: 0 0 40px 40px;
    display: flex;
    align-items: center;
    justify-content: center;
  }
  .flap-url {
    color: #ffffff;
    font-size: 10.5px;
    letter-spacing: 2px;
  }
</style>
</head>
<body>

  <section class="sheet letterhead" aria-label="A4 letterhead">
    <div class="brand">
      <span class="brand-name">Keyhaven Estates</span>
      <span class="brand-dot"></span>
    </div>
    <footer class="contact-bar">
      <div class="contact-block block-address">Suite 7, 18-19 Harlow Parade<br>Brookvale NSW 2100</div>
      <span class="contact-divider divider-one"></span>
      <div class="contact-block block-phones">Tom Carrick 0417 293 608<br>Lorena Adcock 0409 516 742</div>
      <span class="contact-divider divider-two"></span>
      <div class="contact-block block-web">info@keyhavenestatesgroup.com.au<br>www.keyhavenestatesgroup.com.au</div>
    </footer>
    <div class="edge-stripe"></div>
  </section>

  <section class="sheet envelope-front" aria-label="DL envelope front">
    <div class="brand">
      <span class="brand-name">Keyhaven Estates</span>
      <span class="brand-dot"></span>
    </div>
    <footer class="contact-bar">
      <div class="contact-block block-address">Suite 7, 18-19 Harlow Parade<br>Brookvale NSW 2100</div>
      <span class="contact-divider divider-one"></span>
      <div class="contact-block block-phones">Tom Carrick 0417 293 608<br>Lorena Adcock 0409 516 742</div>
      <span class="contact-divider divider-two"></span>
      <div class="contact-block block-web">info@keyhavenestatesgroup.com.au<br>www.keyhavenestatesgroup.com.au</div>
    </footer>
    <div class="edge-stripe"></div>
  </section>

  <section class="sheet envelope-back" aria-label="DL envelope back">
    <div class="flap">
      <span class="flap-url">www.keyhavenestatesgroup.com.au</span>
    </div>
  </section>

</body>
</html>
```